Unique Book Cover for Colors (Front, Spine Back and 1 page spread for inside)

We are looking for a creative design for book cover with harmonious colors.
It should be contemporary, stylish and clean that will grab the attention of the clients.

Must have a unique layout perhaps consisting of:

- Beautiful sceneries of nature
- Anything inspired from nature
- Which also has a well planned and thought of color combination.

Must:

1. Use the size w = 14.5cm xh = 20cm spine = 6cm.

2. Logo must be in the upper middle. (See attachment)

3. Front and back cover must have a meaning. We would like it to come across as serious and professional, yet very personable and modern.(unique front & back cover)

4. Create a text "Tint Harbor" (front and spine only)

5. Also attached is the template for the inside spread page. Use that as a reference for your creative idea.

6. Please use the attached text (address)for the back cover. (must be in the middle bottom of the page).

7. Design must invoke a sense of peaceful emotion

8. Overall design must not be cluttered.

History of the Company
Al-Nakheel Coatings Company, was established in Riyadh, the capital of the Kingdom of Saudi Arabia, in 1979, as a small company with high aspirations and ambitions. In a short period of time, and as a result of the vision and dedication of the founders, the efforts have succeeded in laying strong grounds for a pioneering company in the paint industry in the GCC countries and the Middle East at large. In this context, the company became a pioneer in manufacturing and developing innovative, high quality and environmentally responsible paints, designed to meet the requirements and needs of a wide range of clients including industrial, commercial and individuals.

Looking forward to see your creative ideas....

ENJOY!!

Target Market(s)

Corporate, Urban, Real Estate

Industry/Entity Type

Paint

Font styles to use
Serif
Sans Serif
Decorative
Script
Other font styles liked:
• Arial, Helvetica thin 35

Requirements
Must have
• 1. Use the size w = 14.5cm xh = 20cm spine = 6cm.

Should not have
• people and animals

```html
<!DOCTYPE html>
<html lang="en">
<head>
<meta charset="utf-8">
<title>Tint Harbor — Al-Nakheel Coatings Company</title>
<link href="https://fonts.googleapis.com/css2?family=Poiret+One&family=Montserrat:wght@500;600&family=Cairo:wght@500&family=Great+Vibes&display=swap" rel="stylesheet">
<style>
  :root {
    --paper: #e1e3e2;
    --spine: #e6e8e7;
    --title-red: #d8232a;
    --band: #262626;
    --band-text: #ffffff;
    --badge: #d9d9d9;
    --blue: #1f8fc4;
    --yellow: #f5c629;
    --pink: #e8315f;
    --orange: #f0781e;
    --purple: #6a2d8c;
    --leaf: #6aa82a;
  }
  * { box-sizing: border-box; margin: 0; padding: 0; }
  html, body { width: 1200px; height: 712px; overflow: hidden; background: var(--paper); }
  .cover {
    position: relative;
    width: 1200px;
    height: 712px;
    display: flex;
    font-family: "Poiret One", sans-serif;
  }

  /* Back cover */
  .back {
    position: relative;
    width: 569px;
    height: 712px;
  }
  .back-visual {
    position: absolute;
    inset: 0 0 62px 0;
    background:
      radial-gradient(circle at 35% 35%, var(--pink) 0 12%, transparent 28%),
      radial-gradient(circle at 45% 52%, var(--blue) 0 14%, transparent 32%),
      radial-gradient(circle at 15% 60%, var(--orange) 0 10%, transparent 26%),
      radial-gradient(circle at 60% 12%, var(--yellow) 0 10%, transparent 28%),
      radial-gradient(circle at 55% 85%, var(--purple) 0 10%, transparent 28%),
      linear-gradient(135deg, var(--blue), var(--yellow) 45%, var(--blue) 75%, var(--purple));
  }
  .back-band {
    position: absolute;
    left: 0; right: 0; bottom: 0;
    height: 62px;
    background: var(--band);
    color: var(--band-text);
    display: flex;
    align-items: center;
    padding: 0 28px 0 78px;
  }
  .badges { display: flex; gap: 5px; margin-right: 22px; }
  .badge { width: 17px; height: 17px; border-radius: 50%; background: var(--badge); }
  .contact { flex: 1; text-align: center; font-family: "Montserrat", sans-serif; }
  .contact-web { font-size: 15px; font-weight: 600; letter-spacing: 0.3px; }
  .contact-social { display: flex; justify-content: center; gap: 12px; margin-top: 6px; font-size: 7.5px; font-weight: 500; }
  .handle { display: flex; align-items: center; gap: 4px; }
  .handle::before { content: ""; width: 11px; height: 11px; background: var(--badge); border-radius: 2px; }
  .tagline { text-align: center; margin-left: 18px; white-space: nowrap; }
  .tagline-ar { font-family: "Cairo", sans-serif; font-size: 14px; line-height: 1.1; }
  .tagline-en { font-family: "Great Vibes", cursive; font-size: 12px; line-height: 1.1; }

  /* Spine */
  .spine {
    width: 58px;
    height: 712px;
    background: var(--spine);
    display: flex;
    justify-content: center;
    padding-top: 16px;
  }
  .spine-title {
    writing-mode: vertical-rl;
    color: var(--title-red);
    font-size: 56px;
    letter-spacing: 20px;
    line-height: 1;
    white-space: nowrap;
  }

  /* Front cover */
  .front {
    position: relative;
    flex: 1;
    height: 712px;
    background: var(--paper);
  }
  .brand {
    position: absolute;
    top: 38px; left: 0; right: 0;
    display: flex; justify-content: center; align-items: center; gap: 10px;
    color: var(--title-red);
    font-size: 22px;
  }
  .brand-dot { width: 34px; height: 34px; border-radius: 50%; background: var(--leaf); }
  .front-title {
    position: absolute;
    top: 112px; left: 0; right: 0;
    text-align: center;
    color: var(--title-red);
    font-size: 46px;
    font-weight: 400;
    letter-spacing: 8px;
    white-space: nowrap;
  }
  .front-visual { position: absolute; left: 60px; top: 200px; width: 513px; height: 512px; }
</style>
</head>
<body>
  <main class="cover">
    <section class="back">
      <div class="back-visual" role="img" aria-label="Close-up photograph of a folded paper flower ball in blue, yellow, pink, orange and purple"></div>
      <footer class="back-band">
        <div class="badges">
          <span class="badge"></span><span class="badge"></span><span class="badge"></span><span class="badge"></span>
        </div>
        <div class="contact">
          <div class="contact-web">www.nakheelcoatings.com</div>
          <div class="contact-social">
            <span class="handle">nakheelcoatings</span>
            <span class="handle">nakheelcoatingsCo</span>
            <span class="handle">nakheelcoatings</span>
          </div>
        </div>
        <div class="tagline">
          <div class="tagline-ar" lang="ar">لون وعناية</div>
          <div class="tagline-en">Color &amp; Care</div>
        </div>
      </footer>
    </section>

    <aside class="spine">
      <div class="spine-title">TINT HARBOR</div>
    </aside>

    <section class="front">
      <div class="brand">
        <span class="brand-dot"></span>
        <span class="brand-name">Al-Nakheel Coatings Company</span>
      </div>
      <h1 class="front-title">TINT HARBOR</h1>
      <svg class="front-visual" viewBox="0 0 513 512" role="img" aria-label="Illustration of a flock of origami paper birds fading from yellow and green to blue and red">
        <defs>
          <linearGradient id="flock" x1="0" y1="0" x2="1" y2="1">
            <stop offset="0" stop-color="#e2cf2a"/>
            <stop offset="0.3" stop-color="#6aa82a"/>
            <stop offset="0.6" stop-color="#1f5fbf"/>
            <stop offset="1" stop-color="#d8232a"/>
          </linearGradient>
        </defs>
        <polygon points="0,0 130,0 513,190 513,512 0,512" fill="url(#flock)" opacity="0.9"/>
      </svg>
    </section>
  </main>
</body>
</html>
```